50 Page Catalog Full Redesign New Look

We are looking for a redesign of our Catalog,

We are looking for a modern redesign of our Catalog, with our new logo most of the products will be the same with some new products as well.
Please use colors in the new logo attached
Attached is our current design please see this for what product will go in the catulog
Updates

Designs look the same

Target Market(s)

Automotive

Font styles to use
Other font styles liked:
• Our Font is outfit

Colors

Designer to choose colors to be used in the design.

```html
<!DOCTYPE html>
<html lang="en">
<head>
<meta charset="UTF-8">
<title>Oskavel Promotional – 2021 Automotive Catalogue Cover</title>
<link href="https://fonts.googleapis.com/css2?family=Outfit:wght@300;400;500;600&display=swap" rel="stylesheet">
<style>
  :root {
    --page-bg: #efefef;
    --back-blue-light: #5b9fc5;
    --back-blue-dark: #3f87b3;
    --front-blue: #15628f;
    --front-blue-edge: #1a6996;
    --ink-light: #ffffff;
    --year-grey: #e3e3e3;
    --hero-red: #d9435a;
    --hero-violet: #5a4a6a;
    --hero-steel: #8c95a8;
    --hero-yellow: #e9c431;
    --hero-orange: #e68a2e;
  }
  * { margin: 0; padding: 0; box-sizing: border-box; }
  html, body {
    width: 1200px; height: 800px; overflow: hidden;
    background: var(--page-bg);
    font-family: "Outfit", sans-serif;
  }
  .catalogue-spread {
    position: absolute; left: 80px; top: 22px;
    width: 1040px; height: 756px;
    display: flex;
  }
  .cover-page { position: relative; width: 520px; height: 100%; }
  .cover-page--back {
    background: linear-gradient(135deg, var(--back-blue-light), var(--back-blue-dark));
  }
  .cover-page--front {
    background: linear-gradient(90deg, var(--front-blue-edge), var(--front-blue));
  }
  .hero-band {
    position: absolute; left: 0; top: 190px;
    width: 1040px; height: 377px;
    background:
      radial-gradient(ellipse 22% 40% at 50% 55%, rgba(220,225,235,0.85), rgba(140,149,168,0) 70%),
      linear-gradient(90deg, var(--hero-red) 0%, #c2506c 22%, var(--hero-violet) 38%, var(--hero-steel) 50%, #b89a4a 64%, var(--hero-yellow) 76%, var(--hero-orange) 100%);
  }
  .brand {
    position: absolute; left: 0; right: 0; top: 34px;
    display: flex; flex-direction: column; align-items: center;
    color: var(--ink-light);
  }
  .brand-mark {
    width: 72px; height: 72px; border-radius: 50%;
    border: 4px solid var(--ink-light);
  }
  .brand-name {
    margin-top: 6px; font-size: 33px; font-weight: 500;
    letter-spacing: 2px; line-height: 1;
  }
  .brand-tagline {
    margin-top: 3px; font-size: 13px; font-weight: 500;
    letter-spacing: 1px; line-height: 1;
    display: flex; align-items: center; gap: 8px;
  }
  .brand-tagline::before, .brand-tagline::after {
    content: ""; width: 16px; height: 1.5px; background: var(--ink-light);
  }
  .website {
    position: absolute; left: 0; right: 0; top: 596px;
    text-align: center; color: var(--ink-light);
    font-size: 20px; font-weight: 400; letter-spacing: 0.3px;
  }
  .edition-year {
    position: absolute; left: 132px; top: 562px;
    font-size: 122px; font-weight: 600; line-height: 1;
    letter-spacing: -2px; color: var(--year-grey);
  }
  .edition-title {
    position: absolute; left: 137px; top: 705px;
    font-size: 20px; font-weight: 400; color: var(--ink-light);
  }
</style>
</head>
<body>
  <main class="catalogue-spread">
    <section class="cover-page cover-page--back">
      <p class="website">oskavelpromotional.com.au</p>
    </section>
    <section class="cover-page cover-page--front">
      <div class="brand">
        <div class="brand-mark"></div>
        <div class="brand-name">OSKAVEL</div>
        <div class="brand-tagline">PROMOTIONAL</div>
      </div>
      <h1 class="edition-year">2021</h1>
      <p class="edition-title">Automotive Products &amp; Ideas</p>
    </section>
    <div class="hero-band" role="img" aria-label="Front view of a red and yellow sports car dissolving into a burst of colourful pixel squares"></div>
  </main>
</body>
</html>
```